Strategy and Technology Consulting - Our Story and Values Page

Interior Page design – Our History and Our Values

Our homepage has been designed and we are looking for a design for one of the interior pages. This interior page tells the story of Our History and Our Values

Because the homepage has been designed, we would like this interior page to reflect the design of the homepage without being a mirror image of the homepage.

This site will be implemented in WordPress using the Elementor framework.

Font: Poppins medium and Poppins dark
Illustrations: Our homepage illustrations were designed by “Welmo 1974” on Pixaborne. Compatible original or stock illustrations are welcome. Stock photography is also welcome. Welmo is also available through Welmo Trastek on Folivane

Uploaded Files
• Homepage design – this is the design we will use for our homepage. Contest entries should reflect this basic style but should be distinctly different from the homepage.
• Our History and Our Values – Wireframe – the basic layout of the page we are looking for.
• Our History and Our Values – Word document with the text supporting the wireframe.
• Color Palette – please use colors compatible with the palette attached.

Our Story - timeline
There is a timeline element in the wireframe. The wireframe displays this as a series of chevrons (arrows), but it does not need to be. Creativity in display of the timeline is appreciated.

Our Values
If you look at the Word document, you will see that there are a lot of words on the page. The winning design will present the information in a way that engages the user without overwhelming them with too much to read. For example, they may click on a value and see more information.

Target Market(s)

CIO's and Technology Executives

Number of Pages Required

1 page

Font styles to use
Sans Serif
Other font styles liked:
• Poppin

Requirements
Must have
• A timeline element, all of our values
Nice to have
• Clever timeline display

```html
<!DOCTYPE html>
<html lang="en">
<head>
<meta charset="utf-8">
<title>Altivex – Our Story and Values</title>
<link href="https://fonts.googleapis.com/css2?family=Poppins:wght@400;500;600;700&display=swap" rel="stylesheet">
<style>
:root{
  --ink:#3b475e;
  --text:#5a6070;
  --yellow:#f6bd16;
  --yellow-deep:#e9a900;
  --blue:#1f5a8c;
  --blue-soft:#6ea3e6;
  --slate:#485670;
  --slate-dark:#3f4b62;
  --gray-panel:#9eafc4;
  --pale:#f3f5fb;
  --white:#ffffff;
}
*{box-sizing:border-box;margin:0;padding:0}
html,body{width:1200px;height:4773px;overflow:hidden}
body{position:relative;font-family:'Poppins',sans-serif;background:var(--white);color:var(--text)}
.abs{position:absolute}

/* header */
.site-header{position:absolute;left:0;top:0;width:1200px;height:90px}
.site-header .rule{position:absolute;left:15px;right:15px;top:88px;height:1px;background:#eceef3}
.brand{position:absolute;left:105px;top:22px;font-size:40px;font-weight:500;color:#8c95a6;letter-spacing:-0.5px;line-height:1}
.brand-dot{display:inline-block;width:10px;height:10px;background:var(--blue);border-radius:50%;margin-right:6px;vertical-align:middle}
.main-nav{position:absolute;left:538px;top:35px;display:flex;gap:22px;font-size:11.5px;font-weight:600;color:#3b475e;align-items:center}
.main-nav .caret{font-size:9px;margin-left:3px}
.btn-yellow{display:inline-flex;align-items:center;justify-content:center;background:var(--yellow);color:var(--white);font-weight:700;font-size:11px;border-radius:20px;letter-spacing:.3px}
.site-header .btn-yellow{position:absolute;left:960px;top:25px;width:128px;height:37px}

/* headings */
.section-title{position:absolute;left:0;width:1200px;text-align:center;font-size:44px;font-weight:600;color:var(--ink)}

/* timeline */
.timeline{position:absolute;left:111px;top:243px;width:978px;height:366px;display:flex}
.era{position:relative;width:326px;height:366px;padding:38px 0 0 36px;color:var(--white)}
.era h3{font-size:34px;font-weight:600;margin-bottom:22px;letter-spacing:-0.3px}
.era ul{list-style:none;font-size:14.5px;line-height:22px}
.era li{position:relative;padding-left:22px;margin-bottom:22px;max-width:240px}
.era li::before{content:"";position:absolute;left:0;top:5px;width:13px;height:13px;border-radius:50%;background:var(--yellow)}
.era li.sub{padding-left:40px;margin-bottom:22px}
.era li.sub::before{content:"-";background:none;left:22px;top:0;width:auto;height:auto;color:var(--white)}
.era-1{background:var(--gray-panel)}
.era-2{background:var(--blue);padding-left:44px}
.era-3{background:var(--slate);padding-left:50px;box-shadow:-14px 0 18px rgba(0,0,0,.25) inset}
.era-arrow{position:absolute;top:168px;width:50px;height:50px;border-radius:50%;background:var(--yellow);display:flex;align-items:center;justify-content:center;z-index:2}
.era-arrow svg{width:20px;height:20px}

/* values */
.values-bg{position:absolute;left:0;top:660px;width:1200px;height:3500px}
.value-title{position:absolute;font-size:30px;font-weight:600;color:var(--ink);line-height:38px}
.value-body{position:absolute;font-size:14.6px;line-height:27.5px;color:var(--text)}
.art{position:absolute;border-radius:46% 54% 50% 50% / 52% 48% 52% 48%}

/* newsletter + footer */
.footer-bg{position:absolute;left:0;top:4040px;width:1200px;height:733px}
.newsletter{position:absolute;left:137px;top:4064px;width:926px;height:196px;background:var(--yellow);border-radius:98px}
.newsletter h2{position:absolute;left:80px;top:58px;font-size:31px;font-weight:700;color:var(--white)}
.newsletter p{position:absolute;left:80px;top:108px;width:420px;font-size:13.5px;line-height:18px;color:var(--white);font-weight:500}
.subscribe{position:absolute;left:550px;top:76px;width:323px;height:46px;background:var(--white);border-radius:23px;display:flex;align-items:center;padding-left:26px;font-size:12px;color:#9aa1ad}
.subscribe .env{width:13px;height:9px;border:1.5px solid #9aa1ad;border-radius:2px;margin-right:10px}
.subscribe .send{position:absolute;right:6px;top:6px;width:34px;height:34px;border-radius:50%;background:#9aa6b8;display:flex;align-items:center;justify-content:center}

.footer-brand{position:absolute;left:120px;top:4445px;font-size:62px;font-weight:500;color:#e6e9ef;line-height:1;letter-spacing:-1px}
.socials{position:absolute;left:176px;top:4522px;display:flex;gap:13px}
.socials span{width:38px;height:38px;border-radius:50%;background:#5c6880;border:1px solid #6c7890}
.footer .btn-yellow{position:absolute;left:213px;top:4588px;width:132px;height:36px}
.foot-col{position:absolute;top:4420px;color:var(--white)}
.foot-col h4{font-size:19px;font-weight:700;margin-bottom:18px}
.foot-col ul{list-style:none;font-size:12.5px;line-height:31px;color:#dfe3ea}
.foot-col li::before{content:"›";margin-right:8px}
.contact-item{position:relative;padding-left:24px;font-size:12.5px;line-height:18px;color:#dfe3ea;margin-bottom:16px;width:200px}
.contact-item svg{position:absolute;left:0;top:2px;width:14px;height:14px}
.copyright{position:absolute;left:0;top:4739px;width:1200px;text-align:center;font-size:12px;color:#eef0f4;font-weight:500}
.chat{position:absolute;left:1137px;top:4697px;width:46px;height:46px;border-radius:50%;background:var(--yellow);display:flex;align-items:center;justify-content:center}
</style>
</head>
<body>

<header class="site-header">
  <div class="brand"><span class="brand-dot"></span>Altivex</div>
  <nav class="main-nav">
    <svg width="14" height="13" viewBox="0 0 14 13"><path d="M7 1 1 6.5h2V12h3V8.5h2V12h3V6.5h2z" fill="#8c95a6"/></svg>
    <span>ABOUT US<span class="caret">⌄</span></span>
    <span>SERVICES<span class="caret">⌄</span></span>
    <span>INSIGHTS<span class="caret">⌄</span></span>
    <span>JOIN US<span class="caret">⌄</span></span>
  </nav>
  <a class="btn-yellow">CONTACT US</a>
  <div class="rule"></div>
</header>

<h1 class="section-title" style="top:142px">Our Story</h1>

<section class="timeline">
  <div class="era era-1">
    <h3>2017 – 2019</h3>
    <ul>
      <li>Growth Strategy Focus</li>
      <li>Consistent, Modest Growth</li>
      <li>Preliminary Focus on Technology</li>
      <li>Eureka! Implementing strategy is hard.</li>
    </ul>
  </div>
  <div class="era era-2">
    <h3>2020 – 2021</h3>
    <ul>
      <li>Pandemic Pauses Growth</li>
      <li>Rethinking :</li>
      <li class="sub">the business model</li>
      <li class="sub">the delivery model</li>
    </ul>
  </div>
  <div class="era era-3">
    <h3>2022 &amp; Onward</h3>
    <ul>
      <li>Leadership Team for Focus on Essential Areas</li>
      <li>Rapid Growth</li>
      <li>Customer Success</li>
    </ul>
  </div>
  <div class="era-arrow" style="left:301px"><svg viewBox="0 0 20 20"><path d="M7 4l6 6-6 6" stroke="#fff" stroke-width="2.5" fill="none"/></svg></div>
  <div class="era-arrow" style="left:627px"><svg viewBox="0 0 20 20"><path d="M7 4l6 6-6 6" stroke="#fff" stroke-width="2.5" fill="none"/></svg></div>
</section>

<svg class="values-bg" viewBox="0 0 1200 3500" preserveAspectRatio="none" aria-hidden="true">
  <path d="M0 100 C250 180 500 140 700 40 C850 -20 1000 20 1200 20 V3500 H0Z" fill="#f4f6fb"/>
  <path d="M330 150 C500 170 620 80 720 20 C800 -20 880 20 940 60" stroke="#e3e8f2" stroke-width="3" fill="none"/>
</svg>

<h2 class="section-title" style="top:845px">Our Values</h2>

<!-- 1 -->
<div class="art" role="img" aria-label="Illustration: person working at a desk with analytics charts" style="left:10px;top:940px;width:480px;height:420px;background:radial-gradient(circle at 50% 55%,#f6bd16 0 12%,#2f6fd1 13% 30%,#dfe9fb 31% 70%,transparent 71%)"></div>
<h3 class="value-title" style="left:648px;top:992px">The Value of Every Human.<br>Regardless.</h3>
<p class="value-body" style="left:648px;top:1088px;width:445px">Each person's unique experiences and perspectives add vibrant hues to the tapestry of our shared existence. In a world where diversity paints the canvas of humanity, true beauty is found in recognizing the inherent and incalculable value of every human being.</p>

<!-- 2 -->
<h3 class="value-title" style="left:110px;top:1461px">Collaboration</h3>
<p class="value-body" style="left:110px;top:1530px;width:490px">Collaboration in work transforms individual endeavors into symphonies of collective achievement. Through collaboration, diverse talents converge, fostering a rich exchange of ideas that amplifies creativity, accelerates progress, and brings forth solutions beyond what a single mind could conceive.</p>
<div class="art" role="img" aria-label="Illustration: team assembling large puzzle pieces with a ladder" style="left:650px;top:1320px;width:550px;height:460px;background:radial-gradient(circle at 55% 55%,#f6bd16 0 14%,#3d75c9 15% 34%,#e3ecfa 35% 68%,transparent 69%)"></div>

<!-- 3 -->
<div class="art" role="img" aria-label="Illustration: people learning on laptops around a stack of books" style="left:0;top:1790px;width:610px;height:340px;background:radial-gradient(ellipse at 45% 60%,#f6bd16 0 10%,#2f6fd1 11% 30%,#e3ecfa 31% 68%,transparent 69%)"></div>
<h3 class="value-title" style="left:657px;top:1879px">Passion</h3>
<p class="value-body" style="left:657px;top:1934px;width:440px">Passion infuses our work with energy, transforming routine tasks into opportunities for creativity and innovation. Fueled by passion, individuals become unstoppable forces, driven to overcome challenges and achieve remarkable outcomes that benefit them and inspire those around them</p>

<!-- 4 -->
<h3 class="value-title" style="left:110px;top:2301px">Excellence</h3>
<p class="value-body" style="left:110px;top:2370px;width:445px">Excellence isn't a destination; it's a continuous journey of refinement and growth. Striving for excellence cultivates a culture of continuous improvement, fostering innovation, credibility, and a lasting impact that resonates far beyond the immediate task.</p>
<div class="art" role="img" aria-label="Illustration: team reaching up to catch golden stars" style="left:570px;top:2170px;width:630px;height:410px;background:radial-gradient(circle at 55% 45%,#f6bd16 0 16%,#2d4f9e 17% 32%,#e3ecfa 33% 68%,transparent 69%)"></div>

<!-- 5 -->
<div class="art" role="img" aria-label="Illustration: person pushing a large gear up rising steps" style="left:10px;top:2570px;width:500px;height:460px;border-radius:18px;background:linear-gradient(160deg,#f3f6fc 0 35%,#6ea3e6 36% 70%,#3f79cc 71%)"></div>
<h3 class="value-title" style="left:648px;top:2714px">Tenacity</h3>
<p class="value-body" style="left:648px;top:2776px;width:445px">Tenacity is the unwavering anchor that keeps us grounded amidst adversity, propelling us forward when faced with obstacles. The resilience to persist, adapt, and learn from setbacks leads to the mastery of skills and the fulfillment of ambitious goals.</p>

<!-- 6 -->
<h3 class="value-title" style="left:110px;top:3161px">Solution Mindset</h3>
<p class="value-body" style="left:110px;top:3230px;width:490px">A solution mindset is the compass that directs our focus from problems to possibilities. It empowers us to navigate challenges with a proactive mindset, igniting a journey of exploration and innovation that not only resolves issues but also paves the way for continuous growth and success.</p>
<div class="art" role="img" aria-label="Illustration: people with tools on connected puzzle platforms under a lightbulb" style="left:620px;top:2970px;width:580px;height:490px;background:radial-gradient(circle at 50% 60%,#f6bd16 0 8%,#3566b8 9% 34%,#e3ecfa 35% 68%,transparent 69%)"></div>

<!-- 7 -->
<div class="art" role="img" aria-label="Illustration: two people sharing content around a large smartphone" style="left:0;top:3460px;width:590px;height:540px;background:radial-gradient(circle at 50% 50%,#f6bd16 0 9%,#2f5fc4 10% 34%,#e3ecfa 35% 68%,transparent 69%)"></div>
<h3 class="value-title" style="left:657px;top:3601px">Generosity</h3>
<p class="value-body" style="left:657px;top:3656px;width:440px">Generosity creates a virtuous cycle of goodwill, fostering a sense of unity and shared purpose among colleagues. By freely sharing knowledge, support, and resources, we uplift those around us and contribute to a collaborative environment where collective achievements flourish.</p>

<!-- footer -->
<svg class="footer-bg" viewBox="0 0 1200 733" preserveAspectRatio="none" aria-hidden="true">
  <path d="M0 40 C300 160 700 130 900 60 C1020 20 1120 30 1200 60 V733 H0Z" fill="var(--slate)"/>
</svg>

<section class="newsletter">
  <h2>Subscribe Our Newsletter</h2>
  <p>Subscribe our newsletter to receive the latest news and exclusive offers every week, No spam.</p>
  <div class="subscribe"><span class="env"></span>Enter email address
    <span class="send"><svg width="14" height="14" viewBox="0 0 14 14"><path d="M1 7 13 1 9 13 7 8z" fill="#fff"/></svg></span>
  </div>
</section>

<footer class="footer">
  <div class="footer-brand">Altivex</div>
  <div class="socials"><span></span><span></span><span></span><span></span></div>
  <a class="btn-yellow">CONTACT US</a>

  <div class="foot-col" style="left:490px">
    <h4>Quick links</h4>
    <ul><li>Home</li><li>About Us</li><li>Services</li><li>Insights</li><li>Join Us</li><li>Contact Us</li></ul>
  </div>
  <div class="foot-col" style="left:668px">
    <h4>Our Services</h4>
    <ul><li>Business Transformation</li><li>ERP Implementations</li><li>ERP Solutions</li><li>BI and Data</li><li>Building the Right Team...</li></ul>
  </div>
  <div class="foot-col" style="left:900px">
    <h4>Contact info</h4>
    <div class="contact-item"><svg viewBox="0 0 14 14"><rect x="1" y="3" width="12" height="8" rx="1" fill="#f6bd16"/></svg>Email:<br>hello@altivexgroup.com</div>
    <div class="contact-item"><svg viewBox="0 0 14 14"><path d="M3 1l3 3-2 2c1 2 2 3 4 4l2-2 3 3-2 2C6 13 1 8 1 3z" fill="#f6bd16"/></svg>Phone:<br>+44 100 555 0142</div>
    <div class="contact-item"><svg viewBox="0 0 14 14"><path d="M7 1a4 4 0 0 1 4 4c0 3-4 8-4 8S3 8 3 5a4 4 0 0 1 4-4z" fill="#f6bd16"/><circle cx="7" cy="5" r="1.5" fill="#485670"/></svg>Location:<br>Some address line goes here city name</div>
  </div>

  <p class="copyright">© Altivex Design 2023, All Rights Reserved</p>
  <div class="chat"><svg width="22" height="20" viewBox="0 0 22 20"><path d="M11 2C6 2 2 5 2 9c0 2 1 4 3 5l-1 4 4-2c1 .3 2 .4 3 .4 5 0 9-3 9-7s-4-7-9-7z" fill="#fff"/></svg></div>
</footer>

</body>
</html>
```